TRVL-NINE Web Design

We are a Health, Safety, Environmental & Quality Recruitment Agency, our clients are major corporate Mining, Oil & Gas and Engineering companies. We have offices in Perth & Melbourne, Australia

The website should be very functional & easy to navigate

BUT REALLY LOOKING FOR WOW FACTOR!

Please Note: TRVL CORPORATE IS OUR OLD COMPANY THE NEW ONE IS "TRVL-NINE" 

Some idea's from our competitors:

http://www.guardlinepeak.com.au/
http://www.vantagehiring.com.au/
http://www.brightpick.com.au/
http://www.kovastaffing.co.uk/
http://www.jobmarrow.com/health-safety-environment-jobs

Would love to see some of our valued clients and there logos

still looking for wow factor

Industry/Entity Type

Mining

Requirements
Must have
• A place where candidates can upload there resumes & other contact details
• eg: http://www.guardlinepeak.com.au/candidates/register-your-resume/
• A place we can load jobs on to eg: http://www.guardlinepeak.com.au/vacancies/
• Contact details:
• Perth: 12 Kestrel Ave, West Perth, Western Australia 6005
• t: 08 7153 4406 | f: 08 7153 4470 |
• Melbourne: Level 1, 218 Arbour Lane, Melbourne, Victoria 3000
• t: 03 6214 5072| f: 03 6231 4095 |
• e: dennisk@trvlnine.com.au | w: http://www.trvlnine.com.au

```html
<!DOCTYPE html>
<html lang="en">
<head>
<meta charset="utf-8">
<title>TRVL-NINE | Recruiting for all standards</title>
<link href="https://fonts.googleapis.com/css2?family=Open+Sans:wght@400;600;700&family=Oswald:wght@500;600&display=swap" rel="stylesheet">
<style>
:root{
  --blue:#1f86cf;
  --blue-dark:#136aa8;
  --orange:#e8731f;
  --ink:#333;
  --muted:#777;
  --line:#e3e3e3;
  --panel:#f3f3f3;
  --footer:#2c2c2c;
  --footer-deep:#1e1e1e;
  --footer-text:#bdbdbd;
}
*{box-sizing:border-box;margin:0;padding:0}
html,body{width:771px;height:1200px;overflow:hidden}
body{font-family:"Open Sans",Arial,sans-serif;color:var(--ink);background:#fff;font-size:10px;line-height:1.45}

/* header */
.site-header{height:100px;display:flex;justify-content:space-between;align-items:center;padding:0 48px}
.brand{display:flex;align-items:center;gap:10px}
.brand-mark{width:44px;height:44px;background:var(--blue)}
.brand-name{font-size:26px;font-weight:700;color:#4a5a6a;letter-spacing:.5px}
.header-tools{display:flex;flex-direction:column;align-items:flex-end;gap:10px}
.auth{display:flex;gap:6px}
.btn{font-size:9px;font-weight:700;color:#fff;padding:4px 12px;text-transform:uppercase}
.btn-register{background:var(--orange)}
.btn-login{background:#3a3a3a}
.search{width:190px;height:24px;border:1px solid #ccc;display:flex;justify-content:flex-end;align-items:center;padding-right:6px}

/* nav */
.main-nav{height:32px;background:var(--blue);display:flex;padding:0 48px}
.main-nav a{color:#fff;text-decoration:none;font-size:11px;font-weight:600;padding:0 14px;line-height:32px;text-transform:uppercase;white-space:nowrap;flex:none}
.main-nav a.active{background:var(--blue-dark)}

/* hero */
.hero{height:278px;position:relative;background:linear-gradient(180deg,#1b2636 0%,#33445c 35%,#6b6a6e 55%,#c98b4e 72%,#6a4525 85%,#231a13 100%)}
.hero-text{position:absolute;left:77px;top:128px;width:330px}
.hero-title{font-family:"Oswald",sans-serif;font-weight:600;font-size:22px;color:#fff;letter-spacing:.5px;white-space:nowrap}
.hero-sub{font-size:9px;color:#eee;margin-top:4px;line-height:1.4}

/* features */
.features{display:flex;justify-content:space-between;padding:28px 90px 0;height:210px}
.feature{width:160px;text-align:center}
.feature-icon{width:86px;height:86px;border-radius:50%;margin:0 auto 12px;background:radial-gradient(circle at 50% 35%,#ffffff,#dcdcdc);box-shadow:0 3px 6px rgba(0,0,0,.18);display:flex;align-items:center;justify-content:center}
.feature h3{font-size:13px;font-weight:600;margin-bottom:6px}
.feature p{font-size:8.5px;color:var(--muted)}

/* about + vacancies */
.content{display:flex;padding:0 48px;height:180px;gap:14px}
.section-title{font-size:14px;font-weight:600;margin-bottom:10px}
.about{width:540px}
.about-body{display:flex;gap:14px}
.about-photo{width:260px;height:118px;flex:none;background:linear-gradient(135deg,#a7b1bb,#d8d2c8 60%,#8f9aa5)}
.about-text{flex:1;font-size:8.5px;color:var(--muted);line-height:1.55}
.vacancies{flex:1}
.vacancy{border-bottom:1px dotted #ccc;padding-bottom:8px;margin-bottom:8px}
.vacancy h4{font-size:8.5px;color:var(--blue);font-weight:600;display:flex;gap:5px;align-items:baseline}
.vacancy h4::before{content:"";width:5px;height:5px;flex:none;background:var(--orange)}
.vacancy p{font-size:8px;color:var(--muted);margin-top:3px}

/* testimonials */
.testimonials{padding:0 48px;height:160px;display:flex;gap:20px}
.testimonial-list{display:flex;gap:14px;width:420px}
.quote{width:200px}
.quote blockquote{background:var(--panel);border:1px solid var(--line);padding:9px 10px;font-size:8px;color:var(--muted);height:64px}
.quote cite{display:flex;align-items:center;justify-content:flex-end;gap:6px;font-style:normal;font-size:8.5px;margin-top:6px;white-space:nowrap}
.quote cite::before{content:"";width:14px;height:14px;border-radius:50%;background:#c8c8c8}
.partners{display:flex;gap:16px;align-items:center;margin-top:34px}
.badge-a{width:86px;height:62px;background:linear-gradient(#2b2f86,#d23a3a)}
.badge-b{width:80px;height:40px;border-radius:4px;background:#e6e6e6}

/* footer */
.site-footer{background:var(--footer);height:205px;padding:26px 48px 0;display:flex;gap:20px;color:var(--footer-text)}
.office{width:150px}
.site-footer h5{font-size:13px;font-weight:400;color:#fff;margin-bottom:10px}
.office address{font-style:normal;font-size:8px;line-height:1.6;margin-bottom:10px}
.contact-row{display:flex;align-items:center;gap:8px;font-size:8px;margin-bottom:9px;white-space:nowrap}
.follow{flex:1}
.follow p{font-size:8px;margin-bottom:10px}
.socials{display:flex;gap:6px}
.socials span{width:22px;height:22px;display:block}
.copyright{background:var(--footer-deep);height:35px;padding:0 48px;line-height:35px;font-size:8px;color:#999}
</style>
</head>
<body>

<header class="site-header">
  <div class="brand">
    <span class="brand-mark"></span>
    <span class="brand-name">TRVL-NINE</span>
  </div>
  <div class="header-tools">
    <div class="auth">
      <span class="btn btn-register">Register</span>
      <span class="btn btn-login">Login</span>
    </div>
    <div class="search">
      <svg width="10" height="10" viewBox="0 0 10 10"><circle cx="4" cy="4" r="3" fill="none" stroke="#888" stroke-width="1.3"/><line x1="6.3" y1="6.3" x2="9" y2="9" stroke="#888" stroke-width="1.3"/></svg>
    </div>
  </div>
</header>

<nav class="main-nav">
  <a class="active">Home</a><a>About</a><a>Job Seekers</a><a>Employers</a><a>News Vacancies</a><a>Testimonials</a><a>Contact</a><a>FAQ</a>
</nav>

<section class="hero" role="img" aria-label="Oil and gas refinery lit up at dusk">
  <div class="hero-text">
    <h1 class="hero-title">RECRUITING FOR ALL STANDARDS</h1>
    <p class="hero-sub">Sed ut perspiciatis unde omnis iste natus error sit voluptatem accusantium doloremque laudantium totam rem aperiam.</p>
  </div>
</section>

<section class="features">
  <div class="feature">
    <div class="feature-icon">
      <svg width="34" height="40" viewBox="0 0 34 40"><rect x="2" y="2" width="30" height="36" rx="2" fill="none" stroke="#1f86cf" stroke-width="3"/><line x1="8" y1="12" x2="26" y2="12" stroke="#1f86cf" stroke-width="3"/><line x1="8" y1="20" x2="26" y2="20" stroke="#1f86cf" stroke-width="3"/><line x1="8" y1="28" x2="20" y2="28" stroke="#1f86cf" stroke-width="3"/></svg>
    </div>
    <h3>For Candidates</h3>
    <p>Lorem ipsum dolor sit amet adipiscing elit morbi et vulputate tristique arcu pellentesque habitant morbi.</p>
  </div>
  <div class="feature">
    <div class="feature-icon">
      <svg width="38" height="38" viewBox="0 0 38 38"><circle cx="19" cy="12" r="8" fill="#1f86cf"/><path d="M4 36c0-9 7-14 15-14s15 5 15 14z" fill="#1f86cf"/></svg>
    </div>
    <h3>For Employers</h3>
    <p>Lorem ipsum dolor sit amet adipiscing elit morbi et vulputate tristique arcu pellentesque habitant morbi.</p>
  </div>
  <div class="feature">
    <div class="feature-icon">
      <svg width="38" height="38" viewBox="0 0 38 38"><circle cx="19" cy="19" r="16" fill="none" stroke="#1f86cf" stroke-width="3"/><path d="M11 19l6 6 10-12" fill="none" stroke="#1f86cf" stroke-width="3.5"/></svg>
    </div>
    <h3>Register</h3>
    <p>Lorem ipsum dolor sit amet adipiscing elit morbi et vulputate tristique arcu pellentesque habitant morbi.</p>
  </div>
</section>

<section class="content">
  <div class="about">
    <h2 class="section-title">About Us</h2>
    <div class="about-body">
      <div class="about-photo" role="img" aria-label="Recruitment team meeting in an office"></div>
      <p class="about-text">Duis autem vel eum iriure dolor in hendrerit in vulputate velit esse molestie consequat, vel illum dolore eu feugiat nulla facilisis at vero eros et accumsan et iusto odio dignissim qui blandit praesent luptatum zzril delenit augue duis dolore te feugait nulla facilisi. Nam liber tempor cum soluta nobis eleifend option congue nihil imperdiet doming id quod mazim placerat facer possim assum.</p>
    </div>
  </div>
  <aside class="vacancies">
    <h2 class="section-title">Latest Vacancies</h2>
    <div class="vacancy">
      <h4>HSE Advisor / Corvan Island Regulator</h4>
      <p>We are now recruiting experienced HSE advisors for a major oil and gas project.</p>
    </div>
    <div class="vacancy">
      <h4>HSE Advisor Regulator</h4>
      <p>We are now recruiting experienced HSE advisors for a major oil and gas project.</p>
    </div>
  </aside>
</section>

<section class="testimonials">
  <div>
    <h2 class="section-title">Testimonials</h2>
    <div class="testimonial-list">
      <figure class="quote">
        <blockquote>Fusce feugiat malesuada odio. Morbi nunc odio gravida at cursus nec luctus a lorem. Maecenas tristique orci ac sem.</blockquote>
        <cite>Grace Holloway</cite>
      </figure>
      <figure class="quote">
        <blockquote>Fusce feugiat malesuada odio. Morbi nunc odio gravida at cursus nec luctus a lorem. Maecenas tristique orci ac sem.</blockquote>
        <cite>Owen Marsh</cite>
      </figure>
    </div>
  </div>
  <div class="partners">
    <span class="badge-a"></span>
    <span class="badge-b"></span>
  </div>
</section>

<footer class="site-footer">
  <div class="office">
    <h5>Perth Office</h5>
    <address>Suite 7, 316 Harlow Road<br>Kellmont<br>Western Australia 6012</address>
    <div class="contact-row"><svg width="10" height="10" viewBox="0 0 10 10"><path d="M2 1l2 2-1 1.5c.8 1.5 1.5 2.2 2.5 2.5L7 6l2 2-1.5 1.5C4 9 1 6 .5 2.5z" fill="#bdbdbd"/></svg>+61 (0) 8 5012 3381</div>
    <div class="contact-row"><svg width="10" height="10" viewBox="0 0 10 10"><rect x="1" y="3" width="8" height="5" fill="#bdbdbd"/><rect x="3" y="1" width="4" height="2" fill="#bdbdbd"/></svg>+61 (0) 8 5012 3390</div>
    <div class="contact-row"><svg width="10" height="10" viewBox="0 0 10 10"><rect x=".5" y="2" width="9" height="6" fill="none" stroke="#bdbdbd"/><path d="M.5 2l4.5 3.5L9.5 2" fill="none" stroke="#bdbdbd"/></svg>info@trvlnine.com.au</div>
  </div>
  <div class="office">
    <h5>Brisbane Office</h5>
    <address>Suite 7, 316 Harlow Road<br>Kellmont<br>Western Australia 6012</address>
    <div class="contact-row"><svg width="10" height="10" viewBox="0 0 10 10"><path d="M2 1l2 2-1 1.5c.8 1.5 1.5 2.2 2.5 2.5L7 6l2 2-1.5 1.5C4 9 1 6 .5 2.5z" fill="#bdbdbd"/></svg>+61 (0) 8 5012 3381</div>
    <div class="contact-row"><svg width="10" height="10" viewBox="0 0 10 10"><rect x="1" y="3" width="8" height="5" fill="#bdbdbd"/><rect x="3" y="1" width="4" height="2" fill="#bdbdbd"/></svg>+61 (0) 8 5012 3390</div>
    <div class="contact-row"><svg width="10" height="10" viewBox="0 0 10 10"><rect x=".5" y="2" width="9" height="6" fill="none" stroke="#bdbdbd"/><path d="M.5 2l4.5 3.5L9.5 2" fill="none" stroke="#bdbdbd"/></svg>info@trvlnine.com.au</div>
  </div>
  <div class="office">
    <h5>Seoul Office</h5>
    <address>Suite 7, 316 Harlow Road<br>Kellmont<br>Western Australia 6012</address>
    <div class="contact-row"><svg width="10" height="10" viewBox="0 0 10 10"><path d="M2 1l2 2-1 1.5c.8 1.5 1.5 2.2 2.5 2.5L7 6l2 2-1.5 1.5C4 9 1 6 .5 2.5z" fill="#bdbdbd"/></svg>+61 (0) 8 5012 3381</div>
    <div class="contact-row"><svg width="10" height="10" viewBox="0 0 10 10"><rect x="1" y="3" width="8" height="5" fill="#bdbdbd"/><rect x="3" y="1" width="4" height="2" fill="#bdbdbd"/></svg>+61 (0) 8 5012 3390</div>
    <div class="contact-row"><svg width="10" height="10" viewBox="0 0 10 10"><rect x=".5" y="2" width="9" height="6" fill="none" stroke="#bdbdbd"/><path d="M.5 2l4.5 3.5L9.5 2" fill="none" stroke="#bdbdbd"/></svg>info@trvlnine.com.au</div>
  </div>
  <div class="follow">
    <h5>Follow us</h5>
    <p>Follow us to receive our latest news.</p>
    <div class="socials">
      <span style="background:#3b6fa8"></span>
      <span style="background:#2a9fd6"></span>
      <span style="background:#1c7fb8"></span>
      <span style="background:#cc3a2e"></span>
    </div>
  </div>
</footer>
<div class="copyright">Copyright ©2013, All Rights Reserved</div>

</body>
</html>
```